Organic Infographic – "The 4 Dimensions of Transformation"

Overview:
We are a coaching/education brand (Brightmoor Institute) and need a redesigned infographic illustrating our 4-area transformation model. Our current version (attached) uses a rigid, hard-edged triangle/pyramid layout — we want a completely new visual approach that feels organic, soft, and alive, since the topic is human personal development, not a technical process.

Content structure (please keep the wording, redesign the visual form):

4 areas: "Embodiment – The Foundation" and "Focus & Intuition Redefined – The Lens" sit on the same base level. "Heart Centered Living – The Bridge" sits one level above, connecting/enabling the other two. "Becoming Unlimited – The Peak" sits at the top, made possible by Heart Centered Living.
The 4 areas influence and inspire one another — this mutual connection must be visually recognizable (e.g. through overlapping zones, blended color transitions, connecting flowing lines, or similar). Areas may stay visually distinct; the connection between them is what must be shown.
Hierarchy should be expressed mainly through position/arrangement (ascending flow), not through size differences — all 4 areas should carry similar visual weight, since each is equally essential.
A supporting element: "The Brightmoor Methodology" with 3 phases (Phase 1: Awareness & Insight, Phase 2: Integration & Practice, Phase 3: Expansion & Sustainable Growth), each with a short description (text provided below).

Style direction:
Organic, soft, flowing shapes — no sharp angles or rigid geometric triangles. Attached are 3 moodboard references showing the direction we like: overlapping/blended circular shapes, flowing ribbon-style connections, and organic swirl divisions. Please don't copy any of them directly — combine this organic/overlapping visual language with our specific asymmetric hierarchy (2 areas base level + 1 bridge + 1 peak), which none of the references show exactly. This creative translation is the core task.

Icons: Please design one new, unified icon per area (4 total) plus 3 simple icons for the methodology phases — consistent style across all 7, your creative interpretation is welcome.

Typography: Headlines in Arsenal, body text in DM Sans.

Colors: Base palette — Embodiment D09176, Focus & Intuition Redefined B6623E, Heart Centered Living D9866B, Becoming Unlimited 6F7A70, dark text 23211A, light accent EACEC1. Slight adjustments are welcome if they improve visual distinction between areas.

Technical requirements (important):

Final files as vector format (SVG, AI, or EPS), with separated, editable, non-flattened/non-merged layers and paths.
Shapes should consist of simple, closed outline paths — no fine textures, no complex multi-stop gradients, no photorealistic rendering — since the artwork will later be manually redrawn as a whiteboard-animation video.
Primary format: 16:9 landscape. A secondary vertical/mobile version (3 outer areas stacked below the top area) is welcome but optional.

Usage rights: Full commercial usage across website, video, and social media required.

Attachments to include: current draft PDF (for text content and logo reference only — not for layout), our logo file, and the 3 moodboard reference images.

Budget: $100–150 — please let us know if this realistically allows for more designer participation, or advise on adjusting scope/budget

Methodology phase texts (for the 3 supporting icons):

Phase 1: Awareness & Insight
Cultivating self-reflection, identifying patterns, and gaining clarity on personal drivers through introspective practices and data-informed assessment.

Phase 2: Integration & Practice
Applying tools and frameworks, developing new habits, and aligning actions with core values through consistent application and feedback loops.

Phase 3: Expansion & Sustainable Growth
Achieving long-term transformation, exceeding limitations, and fostering resilience through continuous evolution and a purpose-driven approach.

```html
<!DOCTYPE html>
<html lang="en">
<head>
<meta charset="utf-8">
<title>The 4 Dimensions of Transformation – Brightmoor Institute</title>
<link href="https://fonts.googleapis.com/css2?family=Noto+Sans:wght@700&family=Source+Sans+3:wght@300;400;500&family=Ubuntu:ital,wght@0,400;1,300&display=swap" rel="stylesheet">
<style>
:root{
  --page:#FAEDE4;
  --paper:#FFFFFF;
  --ink:#23211A;
  --body:#4E4A45;
  --muted:#8B9189;
  --peak:#6F7A70;
  --focus:#B6623E;
  --embodiment:#D09176;
  --heart:#DFA893;
  --overlap:#A07F6C;
  --accent:#C9704E;
  --accent-light:#FBE9DF;
  --label-light:#FBF0EA;
}
*{margin:0;padding:0;box-sizing:border-box}
html,body{width:1200px;height:1200px;overflow:hidden;background:var(--page)}
.board{position:relative;width:1200px;height:1200px}
.slide{
  position:absolute;left:106px;width:1592px;height:896px;
  background:var(--paper);transform:scale(.6206);transform-origin:0 0;
  box-shadow:0 14px 22px rgba(80,60,50,.28);
  font-family:"Source Sans 3",sans-serif;color:var(--ink);
}
.slide--one{top:32px}
.slide--two{top:611px}
.brand{position:absolute;left:97px;top:50px;display:flex;align-items:center;gap:14px}
.brand-mark{width:76px;height:76px;border-radius:50%;background:var(--embodiment)}
.brand-name{font-family:"Source Sans 3",sans-serif;font-weight:300;font-size:42px;color:var(--muted);letter-spacing:-.5px}
.pillars{position:absolute;right:100px;top:74px;font-size:15px;letter-spacing:4px;color:var(--muted)}
.motto{position:absolute;right:100px;top:154px;text-align:right;font-family:"Ubuntu",sans-serif;font-style:italic;font-weight:300;font-size:27px;line-height:32px;color:var(--peak);letter-spacing:.5px}
.motto-rule{position:absolute;right:106px;width:78px;height:2px;background:var(--accent)}
.title{position:absolute;left:97px;top:230px;font-family:"Noto Sans",sans-serif;font-weight:700;font-size:56px;line-height:56px;color:var(--ink)}
.title-rule{position:absolute;left:95px;top:367px;width:78px;height:2px;background:var(--accent)}
.subtitle{position:absolute;left:95px;top:390px;font-size:20px;line-height:34px;letter-spacing:5px;color:var(--muted)}
.model{position:absolute;left:0;top:0;width:1592px;height:896px}
.area-name{font-family:"Ubuntu",sans-serif;font-size:25px;fill:var(--label-light);text-anchor:middle;letter-spacing:.5px}
.area-role{font-family:"Ubuntu",sans-serif;font-size:16px;fill:var(--label-light);text-anchor:middle;letter-spacing:1px}
.method-head{position:absolute;left:95px;right:100px;top:646px;display:flex;align-items:center;gap:30px}
.method-head::before,.method-head::after{content:"";flex:1;height:1.5px;background:var(--accent)}
.method-title{font-family:"Ubuntu",sans-serif;font-size:30px;color:var(--ink)}
.phase-icon{position:absolute;top:715px;width:106px;height:106px;border-radius:50%;background:var(--accent-light);color:var(--accent);display:flex;align-items:center;justify-content:center}
.phase-icon svg{width:70px;height:70px}
.phase{position:absolute;top:694px;width:330px}
.phase-title{font-size:19px;font-weight:500;line-height:29px;color:var(--ink)}
.phase-text{font-size:19px;font-weight:300;line-height:29px;color:var(--body)}
.link{position:absolute;top:765px;width:36px;height:1.5px;background:var(--accent)}
.link::after{content:"";position:absolute;left:14px;top:-3.5px;width:8px;height:8px;border-radius:50%;background:var(--accent)}
</style>
</head>
<body>
<svg width="0" height="0" style="position:absolute" aria-hidden="true">
  <defs>
    <symbol id="icon-peak" viewBox="0 0 100 100"><g fill="none" stroke="currentColor" stroke-width="2.4" stroke-linecap="round"><circle cx="50" cy="42" r="9"/><path d="M35 95V78a15 15 0 0 1 30 0v17"/><path d="M50 12v10M34 18l5 8M66 18l-5 8M24 32l9 4M76 32l-9 4M22 46h9M69 46h9"/></g></symbol>
    <symbol id="icon-heart" viewBox="0 0 100 100"><g fill="none" stroke="currentColor" stroke-width="2.4" stroke-linecap="round" stroke-linejoin="round"><path d="M50 46C38 37 32 30 32 23a9 9 0 0 1 18-3 9 9 0 0 1 18 3c0 7-6 14-18 23z"/><path d="M22 40v20l16 16v12M32 54l10 10v10M78 40v20L62 76v12M68 54L58 64v10"/></g></symbol>
    <symbol id="icon-eye" viewBox="0 0 100 100"><g fill="none" stroke="currentColor" stroke-width="2.4" stroke-linecap="round"><path d="M18 50c18-20 46-20 64 0-18 20-46 20-64 0z"/><circle cx="50" cy="50" r="9"/><path d="M50 16v8M50 76v8M34 20l4 7M66 20l-4 7M34 80l4-7M66 80l-4-7M10 50h6M84 50h6"/></g></symbol>
    <symbol id="icon-ground" viewBox="0 0 100 100"><g fill="none" stroke="currentColor" stroke-width="2.4" stroke-linecap="round" stroke-linejoin="round"><circle cx="50" cy="34" r="6"/><path d="M50 42v16M38 52l12-6 12 6M30 74c4-12 14-14 20-14s16 2 20 14zM26 80h48"/><path d="M50 12v8M36 18l4 6M64 18l-4 6"/></g></symbol>
    <symbol id="icon-bulb" viewBox="0 0 100 100"><g fill="none" stroke="currentColor" stroke-width="2.4" stroke-linecap="round" stroke-linejoin="round"><path d="M40 66c0-10-10-14-10-26a20 20 0 0 1 40 0c0 12-10 16-10 26z"/><path d="M40 72h20M41 78h18M44 84h12M50 6v8M22 16l6 6M78 16l-6 6M12 40h8M80 40h8"/></g></symbol>
    <symbol id="icon-gear" viewBox="0 0 100 100"><g fill="none" stroke="currentColor" stroke-width="2.4" stroke-linejoin="round"><path d="M44 12h12l2 10 8 4 9-6 8 8-6 9 4 8 10 2v12l-10 2-4 8 6 9-8 8-9-6-8 4-2 10H44l-2-10-8-4-9 6-8-8 6-9-4-8-10-2V44l10-2 4-8-6-9 8-8 9 6 8-4z"/><circle cx="50" cy="50" r="14"/></g></symbol>
    <symbol id="icon-sprout" viewBox="0 0 100 100"><g fill="none" stroke="currentColor" stroke-width="2.4" stroke-linecap="round" stroke-linejoin="round"><path d="M50 78V40M50 56c-6-8-16-10-26-10 0 12 12 18 26 16M50 44c4-12 14-18 28-18 0 16-12 24-28 24"/><path d="M26 84h48M30 90h40"/></g></symbol>
    <linearGradient id="ribbon" x1="0" y1="0" x2="1" y2="1"><stop offset="0" stop-color="#B9BBAE"/><stop offset="1" stop-color="#F0C9B6"/></linearGradient>
    <linearGradient id="field" x1="0" y1="0" x2="0" y2="1"><stop offset="0" stop-color="#D5D2C4"/><stop offset="1" stop-color="#F1D5C7"/></linearGradient>
    <clipPath id="peak-clip-one"><circle cx="898" cy="176" r="122"/></clipPath>
    <clipPath id="peak-clip-two"><circle cx="903" cy="176" r="128"/></clipPath>
    <marker id="arrowhead" viewBox="0 0 10 10" refX="8" refY="5" markerWidth="7" markerHeight="7" orient="auto-start-reverse"><path d="M0 0L10 5 0 10" fill="none" stroke="#B6623E" stroke-width="1.5"/></marker>
  </defs>
</svg>

<main class="board">

  <!-- Version one: ribbon connections -->
  <section class="slide slide--one">
    <div class="brand"><span class="brand-mark"></span><span class="brand-name">Brightmoor Institute</span></div>
    <p class="pillars">PEOPLE I PURPOSE I REAL CHANGE</p>
    <p class="motto">Inner work.<br>A brighter tomorrow.</p>
    <span class="motto-rule" style="top:244px"></span>
    <h1 class="title">The 4 Dimensions<br>of Transformation</h1>
    <span class="title-rule"></span>
    <p class="subtitle">A MORE AWARE,<br>ALIGNED AND<br>FULFILLED YOU</p>

    <svg class="model" viewBox="0 0 1592 896" role="img" aria-label="Four overlapping areas of transformation">
      <path d="M898 50C820 50 770 110 770 200 770 290 700 330 640 370 580 410 575 560 690 595 790 625 830 478 898 478 965 478 1005 625 1105 595 1220 560 1215 410 1155 370 1095 330 1025 290 1025 200 1025 110 975 50 898 50Z" fill="url(#field)"/>
      <g fill="none" stroke="url(#ribbon)" stroke-linecap="round">
        <path d="M800 92C752 150 775 260 740 300 700 345 620 330 580 385" stroke-width="6"/>
        <path d="M565 430C545 520 590 595 665 606" stroke-width="4"/>
        <path d="M745 605C800 585 840 525 898 525 958 525 1000 585 1060 605" stroke-width="6"/>
        <path d="M1040 210C1045 290 1115 330 1180 365 1250 405 1255 520 1195 585" stroke-width="5"/>
      </g>
      <ellipse cx="896" cy="359" rx="146" ry="106" fill="var(--heart)"/>
      <circle cx="698" cy="478" r="117" fill="var(--embodiment)" fill-opacity=".92"/>
      <circle cx="1097" cy="478" r="117" fill="var(--focus)" fill-opacity=".94"/>
      <ellipse cx="896" cy="359" rx="146" ry="106" fill="var(--heart)" fill-opacity=".35"/>
      <circle cx="898" cy="176" r="122" fill="var(--peak)"/>
      <ellipse cx="896" cy="359" rx="146" ry="106" fill="var(--overlap)" clip-path="url(#peak-clip-one)"/>

      <use href="#icon-peak" x="863" y="88" width="70" height="70" color="#FBF0EA"/>
      <text class="area-name" x="898" y="206">Becoming Unlimited</text>
      <text class="area-role" x="898" y="230">The Peak</text>

      <circle cx="892" cy="340" r="42" fill="var(--accent-light)"/>
      <use href="#icon-heart" x="862" y="310" width="60" height="60" color="#C9704E"/>
      <text class="area-name" x="898" y="400">Heart Centered Living</text>
      <text class="area-role" x="898" y="424">The Bridge</text>

      <circle cx="695" cy="443" r="45" fill="var(--accent-light)"/>
      <use href="#icon-ground" x="663" y="411" width="64" height="64" color="#C9704E"/>
      <text class="area-name" x="698" y="513">Embodiment</text>
      <text class="area-role" x="698" y="537">The Foundation</text>

      <circle cx="1097" cy="438" r="48" fill="var(--accent-light)"/>
      <use href="#icon-eye" x="1063" y="404" width="68" height="68" color="#C9704E"/>
      <text class="area-name" x="1097" y="508">Focus &amp; Intuition</text>
      <text class="area-name" x="1097" y="532">Redefined</text>
      <text class="area-role" x="1097" y="556">The Lens</text>
    </svg>

    <div class="method-head"><h2 class="method-title">The Brightmoor Methodology</h2></div>
    <div class="phase-icon" style="left:94px"><svg><use href="#icon-bulb"/></svg></div>
    <div class="phase" style="left:225px"><p class="phase-title">Phase 1: Awareness &amp; Insight</p><p class="phase-text">Cultivating self-reflection, identifying patterns and gaining clarity on personal drivers through introspective practices and data-informed assessment.</p></div>
    <div class="phase-icon" style="left:569px"><svg><use href="#icon-gear"/></svg></div>
    <div class="phase" style="left:701px"><p class="phase-title">Phase 2: Integration &amp; Practice</p><p class="phase-text">Applying tools and frameworks, developing new habits and aligning actions with core values through consistent application and feedback</p></div>
    <div class="phase-icon" style="left:1016px"><svg><use href="#icon-sprout"/></svg></div>
    <div class="phase" style="left:1149px;width:350px"><p class="phase-title">Phase 3: Expansion &amp; Sustainable Growth</p><p class="phase-text">Achieving long-term transformation, exceeding limitations and fostering resilience through continuous evolution and a purpose-driven approach.</p></div>
  </section>

  <!-- Version two: arrow flow -->
  <section class="slide slide--two">
    <div class="brand"><span class="brand-mark"></span><span class="brand-name">Brightmoor Institute</span></div>
    <p class="pillars">PEOPLE I PURPOSE I REAL CHANGE</p>
    <p class="motto">A more aware,<br>aligned and<br>fulfilled you.</p>
    <span class="motto-rule" style="top:276px"></span>
    <h1 class="title">The 4 Dimensions<br>of Transformation</h1>
    <span class="title-rule"></span>
    <p class="subtitle">A MORE AWARE,<br>ALIGNED AND<br>FULFILLED YOU</p>

    <svg class="model" viewBox="0 0 1592 896" role="img" aria-label="Four overlapping areas of transformation with flow arrows">
      <path d="M903 62C835 62 770 110 765 190 760 290 700 340 640 385 570 440 570 580 690 618 790 650 840 500 903 500 965 500 1015 650 1115 618 1235 580 1235 440 1165 385 1105 340 1045 290 1040 190 1035 110 970 62 903 62Z" fill="#EFD9CD"/>
      <path d="M705 300C690 340 665 370 630 395 660 360 680 330 705 300Z M1075 300C1090 340 1120 370 1160 395 1125 360 1105 330 1075 300Z" fill="#F1D3C5"/>
      <ellipse cx="900" cy="406" rx="152" ry="106" fill="var(--heart)"/>
      <circle cx="692" cy="506" r="122" fill="var(--embodiment)" fill-opacity=".92"/>
      <circle cx="1111" cy="506" r="122" fill="var(--focus)" fill-opacity=".94"/>
      <ellipse cx="900" cy="406" rx="152" ry="106" fill="var(--heart)" fill-opacity=".35"/>
      <circle cx="903" cy="176" r="128" fill="var(--peak)"/>
      <ellipse cx="900" cy="406" rx="152" ry="106" fill="var(--overlap)" clip-path="url(#peak-clip-two)"/>

      <g fill="none" stroke="var(--focus)" stroke-width="1.5">
        <path d="M710 278C712 230 725 200 748 171" marker-end="url(#arrowhead)"/>
        <path d="M1086 298C1085 250 1072 215 1050 188" marker-end="url(#arrowhead)"/>
        <path d="M812 584Q901 634 990 584" marker-start="url(#arrowhead)" marker-end="url(#arrowhead)"/>
      </g>

      <use href="#icon-peak" x="866" y="96" width="74" height="74" color="#FBF0EA"/>
      <text class="area-name" x="903" y="222">Becoming Unlimited</text>
      <text class="area-role" x="903" y="247">The Peak</text>

      <circle cx="897" cy="362" r="43" fill="var(--accent-light)"/>
      <use href="#icon-heart" x="866" y="331" width="62" height="62" color="#C9704E"/>
      <text class="area-name" x="903" y="425">Heart Centered Living</text>
      <text class="area-role" x="903" y="450">The Bridge</text>

      <circle cx="688" cy="471" r="48" fill="var(--accent-light)"/>
      <use href="#icon-ground" x="654" y="437" width="68" height="68" color="#C9704E"/>
      <text class="area-name" x="692" y="544">Embodiment</text>
      <text class="area-role" x="692" y="570">The Foundation</text>

      <circle cx="1113" cy="464" r="50" fill="var(--accent-light)"/>
      <use href="#icon-eye" x="1077" y="428" width="72" height="72" color="#C9704E"/>
      <text class="area-name" x="1113" y="539">Focus &amp; Intuition</text>
      <text class="area-name" x="1113" y="564">Redefined</text>
      <text class="area-role" x="1113" y="590">The Lens</text>
    </svg>

    <div class="method-head"><h2 class="method-title">The Brightmoor Methodology</h2></div>
    <div class="phase-icon" style="left:100px"><svg><use href="#icon-bulb"/></svg></div>
    <div class="phase" style="left:219px"><p class="phase-title">Phase 1: Awareness &amp; Insight</p><p class="phase-text">Cultivating self-reflection, identifying patterns and gaining clarity on personal drivers through introspective practices and data-informed assessment.</p></div>
    <span class="link" style="left:540px"></span>
    <div class="phase-icon" style="left:577px"><svg><use href="#icon-gear"/></svg></div>
    <div class="phase" style="left:694px"><p class="phase-title">Phase 2: Integration &amp; Practice</p><p class="phase-text">Applying tools and frameworks, developing new habits and aligning actions with core values through consistent application and feedback</p></div>
    <span class="link" style="left:990px"></span>
    <div class="phase-icon" style="left:1027px"><svg><use href="#icon-sprout"/></svg></div>
    <div class="phase" style="left:1143px;width:350px"><p class="phase-title">Phase 3: Expansion &amp; Sustainable Growth</p><p class="phase-text">Achieving long-term transformation, exceeding limitations and fostering resilience through continuous evolution and a purpose-driven approach.</p></div>
  </section>

</main>
</body>
</html>
```